VALMIKE GROUP

This is a company that provides executive protection. Our motto is "New Era in Protection"... I don't want this to look like other security websites. I want it to be clean and sharp and represent a new era. We are based in the bay area so maybe a picture of San Francisco in the background?
I want it to be able to funnel down a couple different categories.
1. About Us
2. Services (Executive Protection, Covert Protection, Residential Protection & Intelligence)
3. Iron Finch (Training & Consulting)
4. Contact Us
I want it to be very clean and modern. I don't want there to be any pictures of bodyguards with ear pieces like every other website.
Target Market(s)
Ultra High Net Worth Individuals
Coding
Coded - Design and coding required
Number of Pages Required
1 page
Requirements
Must have
- Colors of my Symbol
Nice to have
- City in the background, San Francisco, New York or the Pinehallow Club in Montana.
Should not have
- Should not look like an KVM website or have photos of bodyguards. I want this to be a clean and simple website with my logo

```html
<!DOCTYPE html>
<html lang="en">
<head>
<meta charset="utf-8">
<title>VALMIKE GROUP – New Era in Protection</title>
<link href="https://fonts.googleapis.com/css2?family=Fira+Sans:wght@300;400;500;600&display=swap" rel="stylesheet">
<style>
:root{
  --red:#8b161b;
  --red-deep:#7a1217;
  --blue:#3b44f6;
  --ink:#222226;
  --text:#3a3a3e;
  --muted:#8a8a90;
  --footer:#1e1e20;
  --white:#ffffff;
}
*{margin:0;padding:0;box-sizing:border-box}
html,body{width:1200px;height:3526px;overflow:hidden;background:var(--white)}
body{font-family:"Fira Sans",sans-serif;color:var(--text);position:relative}
.abs{position:absolute}

/* nav */
.brand{left:107px;top:19px;font-size:11px;font-weight:600;color:var(--red);line-height:14px;white-space:nowrap;display:flex;align-items:center;gap:5px}
.brand-dot{width:10px;height:10px;background:var(--red);flex:none;display:block}
.nav-link{top:19px;font-size:12px;color:var(--ink);font-weight:400;white-space:nowrap}
.nav-link.active{color:var(--blue);font-weight:500}
.nav-link.current::after{content:"";position:absolute;left:-2px;right:-2px;top:31px;height:2px;background:var(--red)}
.nav-cta{left:1003px;top:10px;width:90px;height:33px;background:var(--red);color:var(--white);border-radius:3px;font-size:10px;font-weight:500;display:flex;align-items:center;justify-content:center}

/* hero */
.hero-photo{left:0;top:52px;width:1200px;height:523px;clip-path:polygon(0 0,100% 0,100% 482px,0 100%);
  background:linear-gradient(180deg,#e9c6cc 0%,#dcb6c0 30%,#b9a3b3 52%,#8c8690 72%,#6d6b72 100%)}
.hero-title{left:107px;top:228px;font-size:38px;font-weight:600;color:var(--red);white-space:nowrap}
.hero-sub{left:107px;top:282px;width:380px;font-size:15px;line-height:22px;color:var(--ink)}

/* headings */
.section-title{font-size:30px;font-weight:600;color:var(--red);letter-spacing:.5px}
.title-bar{height:3px;background:var(--blue)}
.body-copy{font-size:15px;line-height:22.4px;color:var(--text)}

/* about */
.about-mark{left:188px;top:637px;width:233px;height:203px;display:flex;align-items:center;justify-content:center;gap:8px;white-space:nowrap}
.about-mark span{font-size:20px;font-weight:600;color:var(--red)}
.about-mark i{width:16px;height:16px;background:var(--red);display:block}

/* features */
.features-band{left:0;top:880px;width:1200px;height:461px;clip-path:polygon(0 37px,100% 0,100% 100%,0 100%);
  background:linear-gradient(180deg,#9a2a2f 0%,#8e2227 45%,#a33a3f 100%)}
.features-title{left:0;width:1200px;top:962px;text-align:center;font-size:30px;font-weight:500;color:var(--white);letter-spacing:1px}
.feature-frame{width:151px;height:151px}
.feature-icon{width:60px;height:70px;background:rgba(255,255,255,.22);border-radius:4px}
.feature-label{top:1240px;font-size:15px;font-weight:500;color:var(--white);line-height:23px;white-space:nowrap}

/* iron finch */
.service-name{font-size:22px;font-weight:500;color:var(--ink)}
.service-copy{font-size:13.6px;line-height:20.2px;color:var(--text);width:435px}
.learn-more{font-size:14px;font-weight:500;color:var(--red);padding-bottom:2px;border-bottom:2px solid var(--red)}
.photo-pool{left:131px;top:1499px;width:450px;height:299px;background:linear-gradient(160deg,#3a4656 0%,#2b4e6d 45%,#1d6fa0 70%,#283441 100%)}
.photo-meeting{left:621px;top:1874px;width:449px;height:298px;background:linear-gradient(120deg,#dfe3e6 0%,#c9ced3 40%,#9aa0a6 70%,#e6e4de 100%)}

/* contact */
.contact-band{left:0;top:2282px;width:1200px;height:373px;background:var(--blue);clip-path:polygon(0 30px,100% 0,100% 100%,0 100%)}
.agent-wrap{left:150px;top:2200px;width:500px;height:455px;overflow:hidden}
.agent-circle{left:50px;top:112px;width:388px;height:388px;border-radius:50%;background:var(--red)}
.agent-photo{left:85px;top:19px;width:320px;height:436px;border-radius:48% 48% 22% 22% / 30% 30% 8% 8%;background:linear-gradient(180deg,#d9c3b2 0%,#efefef 38%,#f6f6f6 100%)}
.contact-title{left:696px;top:2330px;font-size:32px;font-weight:500;color:var(--white)}
.field{left:696px;width:288px;height:20px;border-bottom:2px solid var(--white);font-size:12px;color:var(--white);display:flex;justify-content:space-between;align-items:flex-start}
.field svg{width:13px;height:13px}
.submit-btn{left:696px;top:2595px;width:76px;height:29px;background:var(--white);color:var(--blue);border-radius:3px;font-size:11px;font-weight:500;display:flex;align-items:center;justify-content:center}

/* testimonials */
.quote-card{top:2799px;width:360px;height:196px;border:2px solid var(--blue);background:var(--white);text-align:center}
.quote-card.featured{background:var(--red);border-color:var(--red)}
.quote-card::after{content:"";position:absolute;left:50%;bottom:-11px;width:20px;height:20px;background:inherit;border-right:2px solid var(--blue);border-bottom:2px solid var(--blue);transform:translateX(-50%) rotate(45deg)}
.quote-card.featured::after{border-color:var(--red)}
.quote-mark{margin:36px auto 0;width:30px;height:15px;display:flex;gap:6px;justify-content:center}
.quote-mark span{width:11px;height:15px;background:#a9acf7;clip-path:polygon(30% 0,100% 0,100% 100%,0 100%)}
.featured .quote-mark span{background:var(--white)}
.quote-text{margin:24px auto 0;width:290px;font-size:12px;line-height:20px;color:var(--muted);font-weight:300}
.featured .quote-text{color:var(--white)}
.avatar{top:3034px;width:60px;height:60px;border-radius:50%;background:linear-gradient(180deg,#b98a72,#6b5a52)}
.carousel-mark{left:590px;top:3134px;width:20px;height:20px;background:var(--red)}

/* footer */
.footer{left:0;top:3213px;width:1200px;height:313px;background:var(--footer);clip-path:polygon(0 29px,100% 0,100% 100%,0 100%)}
.footer-brand{left:106px;top:3330px;width:200px;text-align:center;font-size:20px;font-weight:600;color:var(--white);white-space:nowrap}
.footer-small{top:3446px;font-size:10px;color:var(--white);white-space:nowrap}
.footer-head{top:3286px;font-size:19px;font-weight:500;color:var(--white)}
.footer-link{font-size:13px;color:var(--white)}
.footer-link.active{color:var(--blue)}
.social-dot{width:13px;height:13px;border-radius:50%;background:var(--white)}
.newsletter-copy{left:869px;top:3328px;width:240px;font-size:13px;line-height:20px;color:var(--white)}
.news-input{left:869px;top:3390px;width:224px;height:44px;background:var(--white);border-radius:3px;font-size:9px;color:#a0a0a6;padding:15px 0 0 14px}
.news-btn{left:1045px;top:3390px;width:48px;height:44px;background:var(--red);border-radius:0 3px 3px 0;display:flex;align-items:center;justify-content:center}
.copyright{left:0;width:1200px;top:3504px;text-align:center;font-size:10px;color:var(--white)}
</style>
</head>
<body>

<!-- navigation -->
<div class="abs brand"><i class="brand-dot"></i>VALMIKE GROUP</div>
<div class="abs nav-link active" style="left:420px">Home</div>
<div class="abs nav-link" style="left:500px">About Us</div>
<div class="abs nav-link current" style="left:597px">Services</div>
<div class="abs nav-link" style="left:691px">Iron Finch</div>
<div class="abs nav-cta">Contact Us</div>

<!-- hero -->
<div class="abs hero-photo" role="img" aria-label="San Francisco skyline at dusk with the bay and bridge"></div>
<h1 class="abs hero-title">New Era in Protection</h1>
<p class="abs hero-sub">Industry Leading Security Company Specializing in making worry free living.</p>

<!-- about -->
<div class="abs about-mark"><i></i><span>VALMIKE GROUP</span></div>
<h2 class="abs section-title" style="left:551px;top:630px">About Us</h2>
<div class="abs title-bar" style="left:551px;top:668px;width:60px;background:var(--red)"></div>
<p class="abs body-copy" style="left:551px;top:688px;width:445px">Lorem ipsum dolor sit amet, consectetur adipiscing elit. In purus urna, maximus eu consequat non, sollicitudin nec nisi. Cras non urna quis metus gravida vestibulum sit amet id felis. Aliquam nec libero at mauris dictum efficitur. Praesent eleifend, erat nec aliquet tincidunt, arcu metus tincidunt felis, at sollicitudin dui ipsum eu lorem. Curabitur ante ligula, congue in lobortis id,</p>

<!-- features -->
<div class="abs features-band" role="img" aria-label="Tree-lined San Francisco street with a red tint"></div>
<h2 class="abs features-title">SMART FEATURES FOR WORRY FREE WORLD</h2>
<div class="abs title-bar" style="left:311px;top:998px;width:172px;background:var(--white)"></div>

<svg class="abs feature-frame" style="left:109px;top:1067px" viewBox="0 0 151 151"><polygon points="1,11 150,1 150,150 1,150" fill="none" stroke="#fff" stroke-width="2"/></svg>
<div class="abs feature-icon" style="left:154px;top:1102px" role="img" aria-label="Executive protection icon"></div>
<div class="abs feature-label" style="left:115px">Executive Protection</div>

<svg class="abs feature-frame" style="left:525px;top:1067px" viewBox="0 0 151 151"><polygon points="1,11 150,1 150,150 1,150" fill="none" stroke="#fff" stroke-width="2"/></svg>
<div class="abs feature-icon" style="left:570px;top:1102px" role="img" aria-label="Covert protection icon"></div>
<div class="abs feature-label" style="left:542px">Covert Protection</div>

<svg class="abs feature-frame" style="left:941px;top:1067px" viewBox="0 0 151 151"><polygon points="1,11 150,1 150,150 1,150" fill="none" stroke="#fff" stroke-width="2"/></svg>
<div class="abs feature-icon" style="left:986px;top:1102px" role="img" aria-label="Residential protection icon"></div>
<div class="abs feature-label" style="left:941px">Residential Protection<br>&amp; Intelligence</div>

<!-- iron finch -->
<h2 class="abs section-title" style="left:0;width:1200px;top:1382px;text-align:center">Iron Finch</h2>
<div class="abs title-bar" style="left:542px;top:1420px;width:44px"></div>

<svg class="abs" style="left:109px;top:1476px" width="271" height="345" viewBox="0 0 271 345"><polygon points="0,0 240,0 271,22 271,323 240,345 0,345" fill="var(--blue)"/></svg>
<div class="abs photo-pool" role="img" aria-label="Swimming pool training session with an instructor stretching"></div>
<h3 class="abs service-name" style="left:661px;top:1498px">Training</h3>
<p class="abs service-copy" style="left:661px;top:1556px">Lorem ipsum dolor sit amet, consectetur adipiscing elit. In purus urna, maximus eu consequat non, sollicitudin nec nisi. Cras non urna quis metus gravida vestibulum sit amet id felis. Aliquam nec libero at mauris dictum efficitur. Praesent eleifend,</p>
<p class="abs service-copy" style="left:661px;top:1658px">Curabitur ante ligula, congue in lobortis id, aliquet sed urna. Aenean a vestibulum libero. Aliquam sed lorem eget nisi consectetur sollicitudin vestibulum non erat. Pellentesque scelerisque eleifend lectus, eu porta ante tristique ut. Pellentesque pulvi hendrerit.</p>
<div class="abs learn-more" style="left:661px;top:1778px">Learn More</div>

<h3 class="abs service-name" style="left:109px;top:1873px">Consulting</h3>
<p class="abs service-copy" style="left:109px;top:1931px">Lorem ipsum dolor sit amet, consectetur adipiscing elit. In purus urna, maximus eu consequat non, sollicitudin nec nisi. Cras non urna quis metus gravida vestibulum sit amet id felis. Aliquam nec libero at mauris dictum efficitur. Praesent eleifend,</p>
<p class="abs service-copy" style="left:109px;top:2032px">Curabitur ante ligula, congue in lobortis id, aliquet sed urna. Aenean a vestibulum libero. Aliquam sed lorem eget nisi consectetur sollicitudin vestibulum non erat. Pellentesque scelerisque eleifend lectus, eu porta ante tristique ut. Pellentesque pulvi hendrerit.</p>
<div class="abs learn-more" style="left:109px;top:2152px">Learn More</div>
<svg class="abs" style="left:821px;top:1851px" width="272" height="345" viewBox="0 0 272 345"><polygon points="31,0 272,0 272,345 31,345 0,323 0,22" fill="var(--red)"/></svg>
<div class="abs photo-meeting" role="img" aria-label="Two businessmen in a meeting at a bright office table"></div>

<!-- contact -->
<div class="abs contact-band"></div>
<div class="abs agent-wrap">
  <div class="abs agent-circle"></div>
  <div class="abs agent-photo" role="img" aria-label="Smiling support agent wearing a headset, arms crossed"></div>
</div>
<h2 class="abs contact-title">Contact Us</h2>
<div class="abs title-bar" style="left:696px;top:2370px;width:68px;background:var(--white)"></div>
<div class="abs field" style="top:2414px">Name<svg viewBox="0 0 14 14"><circle cx="7" cy="4" r="3.2" fill="#fff"/><path d="M1 14c0-4 2.7-6 6-6s6 2 6 6z" fill="#fff"/></svg></div>
<div class="abs field" style="top:2455px">Email<svg viewBox="0 0 14 14"><rect x="0" y="2" width="14" height="10" fill="#fff"/><path d="M0 3l7 5 7-5" fill="none" stroke="#3b44f6" stroke-width="1.3"/></svg></div>
<div class="abs field" style="top:2496px">Phone<svg viewBox="0 0 14 14"><path d="M3 0l3 3-2 2c1 2 3 4 5 5l2-2 3 3-2 3C6 13 1 8 0 2z" fill="#fff"/></svg></div>
<div class="abs field" style="top:2537px">I want to<svg viewBox="0 0 14 14"><path d="M1 4l6 6 6-6" fill="none" stroke="#fff" stroke-width="1.8"/></svg></div>
<div class="abs submit-btn">Submit</div>

<!-- testimonials -->
<h2 class="abs section-title" style="left:0;width:1200px;top:2706px;text-align:center">What Our Clients Say</h2>
<div class="abs title-bar" style="left:443px;top:2742px;width:52px;background:var(--red)"></div>

<div class="abs quote-card" style="left:38px"><div class="quote-mark"><span></span><span></span></div><p class="quote-text">They are the best group I have ever seen. From the day We decided to have a protection by them we just relax. They are extremely helpful and supportive.</p></div>
<div class="abs quote-card featured" style="left:420px"><div class="quote-mark"><span></span><span></span></div><p class="quote-text">They are the best group I have ever seen. From the day We decided to have a protection by them we just relax. They are extremely helpful and supportive.</p></div>
<div class="abs quote-card" style="left:803px"><div class="quote-mark"><span></span><span></span></div><p class="quote-text">They are the best group I have ever seen. From the day We decided to have a protection by them we just relax. They are extremely helpful and supportive.</p></div>

<div class="abs avatar" style="left:187px" role="img" aria-label="Client portrait"></div>
<div class="abs avatar" style="left:570px" role="img" aria-label="Client portrait"></div>
<div class="abs avatar" style="left:952px" role="img" aria-label="Client portrait"></div>

<svg class="abs" style="left:538px;top:3134px" width="26" height="20" viewBox="0 0 26 20"><path d="M25 10H3M11 2L3 10l8 8" fill="none" stroke="var(--blue)" stroke-width="3"/></svg>
<div class="abs carousel-mark"></div>
<svg class="abs" style="left:636px;top:3134px" width="26" height="20" viewBox="0 0 26 20"><path d="M1 10h22M15 2l8 8-8 8" fill="none" stroke="var(--blue)" stroke-width="3"/></svg>

<!-- footer -->
<div class="abs footer"></div>
<div class="abs footer-brand">VALMIKE GROUP</div>
<div class="abs footer-small" style="left:107px">Privacy Policy</div>
<div class="abs footer-small" style="left:191px">|</div>
<div class="abs footer-small" style="left:215px">Terms &amp; Conditions</div>

<div class="abs footer-head" style="left:419px">Quick Links</div>
<div class="abs footer-link active" style="left:419px;top:3331px">Home</div>
<div class="abs footer-link" style="left:419px;top:3361px">About Us</div>
<div class="abs footer-link" style="left:419px;top:3391px;border-bottom:2px solid var(--red)">Services</div>
<div class="abs footer-link" style="left:419px;top:3421px">Iron Finch</div>
<div class="abs footer-link" style="left:419px;top:3451px">Contact Us</div>

<div class="abs footer-head" style="left:638px">Social Media</div>
<div class="abs social-dot" style="left:639px;top:3333px"></div><div class="abs footer-link" style="left:666px;top:3331px">Friendloop</div>
<div class="abs social-dot" style="left:639px;top:3363px"></div><div class="abs footer-link" style="left:666px;top:3361px">Chirpwire</div>
<div class="abs social-dot" style="left:639px;top:3393px"></div><div class="abs footer-link" style="left:666px;top:3391px">Snapframe</div>
<div class="abs social-dot" style="left:639px;top:3423px"></div><div class="abs footer-link" style="left:666px;top:3421px">Workhub</div>

<div class="abs footer-head" style="left:869px">Newsletter</div>
<p class="abs newsletter-copy">Subscribe our Newsletter for tips and latest news</p>
<div class="abs news-input">Enter Your Email Address</div>
<div class="abs news-btn"><svg width="20" height="18" viewBox="0 0 20 18"><path d="M0 8L20 0 16 18 10 12 17 4 8 11z" fill="#fff"/></svg></div>
<div class="abs copyright">©2021 Valmike Group | All Rights Reserved</div>

</body>
</html>
```